Harbor Crest Residential Business Card Design - Logo Provided

business card design - LOGO PROVIDED. private capital fund investing in: commercial real estate (apartments), asset backed lending, private credit, flexible capital

Target Market(s)

private capital: commercial real estate (apartments), asset backed lending, private credit, flexible capital

Industry/Entity Type

alternative asset management

Contact Information for Business Card

logo, name, title, phone number, email and website

Font styles to use
Sans Serif

Colors
0054AA
0677BA
7BADD7
CADEEF
E8F1F8
EB3D1F
EC4F4E
F09395
F8D3D4
FCEDEE

Requirements
Must have
• use of logo on both sides and a qr code on the back

```html
<!DOCTYPE html>
<html lang="en">
<head>
<meta charset="utf-8">
<title>Harbor Crest Residential – Business Card</title>
<link rel="stylesheet" href="https://fonts.googleapis.com/css2?family=Open+Sans:wght@400;700&display=swap">
<style>
  :root {
    --page: #d6dee4;
    --card-front: #dfdfe1;
    --card-back: #f0eff0;
    --red: #bc1515;
    --navy: #1b2a63;
    --ink: #111111;
    --white: #ffffff;
    --faint: #e4d6d8;
    --edge: #1a1a1a;
  }
  * { margin: 0; padding: 0; box-sizing: border-box; }
  html, body { width: 1200px; height: 1200px; overflow: hidden; }
  body {
    background: var(--page);
    font-family: "Open Sans", sans-serif;
    position: relative;
  }
  .card {
    position: absolute;
    left: 262px;
    width: 676px;
    height: 409px;
    border: 2px solid var(--edge);
    overflow: hidden;
    box-shadow: 0 14px 14px -8px rgba(40, 50, 80, 0.45);
  }
  .card--front { top: 130px; background: var(--card-front); }
  .card--back  { top: 629px; background: var(--card-back); }
  .card__band { position: absolute; inset: 0; width: 100%; height: 100%; }

  .brand {
    position: absolute;
    left: 30px;
    top: 62px;
    display: flex;
    align-items: flex-start;
    gap: 16px;
  }
  .brand__mark {
    width: 34px;
    height: 34px;
    background: var(--red);
    margin-top: 8px;
  }
  .brand__name {
    font-weight: 700;
    font-size: 40px;
    line-height: 1.08;
    color: var(--navy);
    letter-spacing: 0.5px;
  }
  .brand--faint .brand__mark { background: var(--faint); }
  .brand--faint .brand__name { color: var(--faint); }

  .contacts {
    position: absolute;
    right: 38px;
    top: 78px;
    list-style: none;
  }
  .contacts__item {
    display: flex;
    justify-content: flex-end;
    align-items: center;
    gap: 14px;
    height: 44px;
    font-size: 22px;
    color: var(--ink);
  }
  .contacts__icon { width: 32px; height: 30px; fill: var(--navy); flex: none; }

  .person {
    position: absolute;
    left: 441px;
    width: 200px;
    top: 248px;
    text-align: center;
  }
  .person__name { font-weight: 700; font-size: 25px; color: var(--navy); line-height: 1.2; }
  .person__title { font-size: 21px; color: var(--ink); line-height: 1.3; }

  .address {
    position: absolute;
    left: 32px;
    top: 340px;
    display: flex;
    align-items: center;
    gap: 10px;
    font-size: 22px;
    color: var(--ink);
  }
  .address__icon { width: 24px; height: 36px; fill: var(--white); }
</style>
</head>
<body>

<section class="card card--front">
  <svg class="card__band" viewBox="0 0 676 409" preserveAspectRatio="none" aria-hidden="true">
    <polygon points="0,276 132,319 401,243 676,247 676,409 0,409" fill="var(--red)"/>
  </svg>

  <div class="brand">
    <span class="brand__mark"></span>
    <p class="brand__name">Harbor Crest<br>Residential</p>
  </div>

  <ul class="contacts">
    <li class="contacts__item">
      <span>000000000000</span>
      <svg class="contacts__icon" viewBox="0 0 24 24"><path d="M6.6 10.8a15.1 15.1 0 0 0 6.6 6.6l2.2-2.2a1 1 0 0 1 1-.25 11.4 11.4 0 0 0 3.6.57 1 1 0 0 1 1 1V20a1 1 0 0 1-1 1A17 17 0 0 1 3 4a1 1 0 0 1 1-1h3.5a1 1 0 0 1 1 1c0 1.25.2 2.45.57 3.57a1 1 0 0 1-.25 1z"/></svg>
    </li>
    <li class="contacts__item">
      <span>info@xxxx.com</span>
      <svg class="contacts__icon" viewBox="0 0 24 20"><path d="M0 2v16h24V2zm2.5 1.5h19L12 11zM1.5 4.4l7 5.6-7 6.2zm21 0v11.8l-7-6.2zM9.7 11 12 12.9 14.3 11l7 6H2.7z"/></svg>
    </li>
    <li class="contacts__item">
      <span>www.domain.com</span>
      <svg class="contacts__icon" viewBox="0 0 24 22"><path d="M12 2A18 18 0 0 0 0 6.8l1.6 1.7a15.6 15.6 0 0 1 20.8 0L24 6.8A18 18 0 0 0 12 2zm0 5a12.5 12.5 0 0 0-8.4 3.3l1.6 1.7a10 10 0 0 1 13.6 0l1.6-1.7A12.5 12.5 0 0 0 12 7zm0 5a7 7 0 0 0-4.8 1.9l1.7 1.7a4.6 4.6 0 0 1 6.2 0l1.7-1.7A7 7 0 0 0 12 12zm0 5.4a2 2 0 1 0 0 4 2 2 0 0 0 0-4z"/></svg>
    </li>
  </ul>

  <div class="person">
    <p class="person__name">NameXxxxx</p>
    <p class="person__title">Titlexxxxx</p>
  </div>

  <p class="address">
    <svg class="address__icon" viewBox="0 0 24 36"><path d="M12 0A12 12 0 0 0 0 12c0 8 12 24 12 24s12-16 12-24A12 12 0 0 0 12 0zm0 16a5 5 0 1 1 0-10 5 5 0 0 1 0 10z"/></svg>
    <span>Your address xxxxxxxxxx</span>
  </p>
</section>

<section class="card card--back">
  <svg class="card__band" viewBox="0 0 676 409" preserveAspectRatio="none" aria-hidden="true">
    <polygon points="0,276 132,319 401,243 676,247 676,409 0,409" fill="var(--red)"/>
  </svg>

  <div class="brand brand--faint">
    <span class="brand__mark"></span>
    <p class="brand__name">Harbor Crest<br>Residential</p>
  </div>
</section>

</body>
</html>
```